Boutique town planning business needs a Business Card design

We need a business card design for a new company called The Zoning Bridgeway. We provide town planning and urban design services to government, business and community groups. We would like to see the designs use the colours in the logo (blue, deep red, green and amber), plenty of white and including black and grey in the writing. The final design should communicate collaboration, creativity and professionalism and that we are approachable.

```html
<!DOCTYPE html>
<html lang="en">
<head>
<meta charset="utf-8">
<title>The Zoning Bridgeway – Business Card</title>
<link href="https://fonts.googleapis.com/css2?family=Open+Sans:wght@400;600;700&display=swap" rel="stylesheet">
<style>
  :root {
    --deep-red: #a8322a;
    --blue: #4a98c4;
    --green: #7aae3c;
    --amber: #e4992a;
    --ink: #1c1c1c;
    --grey: #6b6b6b;
    --paper: #ffffff;
    --backdrop: #e9ecee;
  }
  * { box-sizing: border-box; margin: 0; padding: 0; }
  html, body {
    width: 1200px; height: 994px; overflow: hidden;
    background: var(--backdrop);
    font-family: "Open Sans", Arial, sans-serif;
  }
  .canvas {
    position: relative; width: 1200px; height: 994px;
    display: flex; flex-direction: column; align-items: center; justify-content: center; gap: 40px;
  }
  .card {
    position: relative; width: 760px; height: 434px;
    background: var(--paper);
    box-shadow: 0 4px 14px rgba(0,0,0,0.12);
    overflow: hidden;
  }
  /* Front */
  .brand { position: absolute; display: flex; align-items: center; gap: 16px; }
  .brand-dot { border-radius: 50%; background: var(--blue); flex: none; }
  .brand-name { color: var(--ink); font-weight: 700; line-height: 1.1; }
  .card-front .brand { left: 50px; top: 70px; }
  .card-front .brand-dot { width: 84px; height: 84px; }
  .card-front .brand-name { font-size: 28px; width: 220px; }
  .person { position: absolute; left: 420px; top: 48px; }
  .person-name { color: var(--deep-red); font-size: 30px; font-weight: 400; }
  .person-role { color: var(--ink); font-size: 21px; margin-top: 8px; }
  .contacts { position: absolute; left: 420px; top: 228px; list-style: none; }
  .contacts li {
    display: flex; align-items: center; gap: 12px;
    font-size: 17px; color: var(--ink); height: 36px;
  }
  .contacts svg { width: 16px; height: 16px; fill: var(--ink); flex: none; }
  .colour-band { position: absolute; left: 0; right: 0; bottom: 0; height: 12px; display: flex; }
  .colour-band span { flex: 1; }
  .band-red { background: var(--deep-red); }
  .band-blue { background: var(--blue); }
  .band-green { background: var(--green); }
  .band-amber { background: var(--amber); }
  /* Back */
  .card-back { display: flex; align-items: center; justify-content: center; }
  .card-back .brand { position: static; gap: 24px; }
  .card-back .brand-dot { width: 130px; height: 130px; }
  .card-back .brand-name { font-size: 44px; }
</style>
</head>
<body>
<main class="canvas">
  <section class="card card-front" aria-label="Business card front">
    <div class="brand">
      <span class="brand-dot"></span>
      <span class="brand-name">The Zoning Bridgeway</span>
    </div>
    <div class="person">
      <p class="person-name">Miranda Holloway</p>
      <p class="person-role">Director</p>
    </div>
    <ul class="contacts">
      <li><svg viewBox="0 0 24 24"><path d="M6.6 10.8a15.1 15.1 0 0 0 6.6 6.6l2.2-2.2c.3-.3.7-.4 1-.2 1.1.4 2.3.6 3.6.6.6 0 1 .4 1 1V20c0 .6-.4 1-1 1A17 17 0 0 1 3 4c0-.6.4-1 1-1h3.5c.6 0 1 .4 1 1 0 1.3.2 2.5.6 3.6.1.3 0 .7-.2 1z"/></svg>ABN 58317490265</li>
      <li><svg viewBox="0 0 24 24"><path d="M6.6 10.8a15.1 15.1 0 0 0 6.6 6.6l2.2-2.2c.3-.3.7-.4 1-.2 1.1.4 2.3.6 3.6.6.6 0 1 .4 1 1V20c0 .6-.4 1-1 1A17 17 0 0 1 3 4c0-.6.4-1 1-1h3.5c.6 0 1 .4 1 1 0 1.3.2 2.5.6 3.6.1.3 0 .7-.2 1z"/></svg>0412 585 307</li>
      <li><svg viewBox="0 0 24 24"><path d="M2 5h20v14H2z" fill="none"/><path d="M2 6l10 7 10-7v13H2z"/><path d="M2 5h20l-10 7z"/></svg>thezoningbridgeway@mailbox.com</li>
      <li><svg viewBox="0 0 24 24"><path d="M12 2a10 10 0 1 0 0 20 10 10 0 0 0 0-20zm6.9 6h-3a15 15 0 0 0-1.3-3.9A8 8 0 0 1 18.9 8zM12 4c.8 1.2 1.5 2.5 1.9 4h-3.8c.4-1.5 1.1-2.8 1.9-4zM4.3 14a8 8 0 0 1 0-4h3.4a16 16 0 0 0 0 4zm.8 2h3a15 15 0 0 0 1.3 3.9A8 8 0 0 1 5.1 16zm3-8h-3a8 8 0 0 1 4.3-3.9C8.8 5.3 8.4 6.6 8.1 8zM12 20c-.8-1.2-1.5-2.5-1.9-4h3.8c-.4 1.5-1.1 2.8-1.9 4zm2.3-6H9.7a14 14 0 0 1 0-4h4.6a14 14 0 0 1 0 4zm.3 5.9c.6-1.2 1-2.5 1.3-3.9h3a8 8 0 0 1-4.3 3.9zm1.7-5.9a16 16 0 0 0 0-4h3.4a8 8 0 0 1 0 4z"/></svg>www.thezoningbridgeway.com.au</li>
    </ul>
    <div class="colour-band">
      <span class="band-red"></span><span class="band-blue"></span><span class="band-green"></span><span class="band-amber"></span>
    </div>
  </section>
  <section class="card card-back" aria-label="Business card back">
    <div class="brand">
      <span class="brand-dot"></span>
      <span class="brand-name">The Zoning Bridgeway</span>
    </div>
  </section>
</main>
</body>
</html>
```